Willowmere Counseling (Endure - Mend - Flourish) - Double Sided Business Card

I would like a 2-sided business card. Front: Matte Black or Navy with Logo & Tagline. Back: Name, Address, Phone Number, Email, & Website (maybe would like to include a small map pin-pointing location); Prefer front to be a gold/silver foil (iridescent); Back prefer white or light colored background with lettering that is easy to read and simple

Target Market(s)

Individuals & Couples (13 y.o. - ALL Adults); High end clientele

Industry/Entity Type

Licensed Professional Counselor (Mental Health)

Contact Information for Business Card

Name: Willowmere Counseling; Tagline: Endure - Mend - Flourish; Address: 3870 N. Garrick Ave., Suite 214, Fort Worth, TX 76132; Phone: (214) 555-0187; Website: www.WillowmereCounseling.example

Font styles to use
Serif

Requirements
Must have
• Logo on Front (Large) prefer gold/silver foil on a matte dark color (i.e. black, navy, etc.); Back of Card: All other relevant information

```html
<!DOCTYPE html>
<html lang="en">
<head>
<meta charset="utf-8">
<title>Willowmere Counseling – Business Card</title>
<link rel="stylesheet" href="https://fonts.googleapis.com/css2?family=Tinos:ital,wght@0,400;0,700;1,400&display=swap">
<style>
  :root {
    --backdrop: #fad592;
    --teal: #3a9fbb;
    --gold: #d8b24a;
    --white: #ffffff;
    --ink: #2e2e2e;
    --body-font: "Tinos", "Times New Roman", serif;
  }
  * { margin: 0; padding: 0; box-sizing: border-box; }
  html, body { width: 1200px; height: 800px; overflow: hidden; }
  body {
    background: var(--backdrop);
    font-family: var(--body-font);
    position: relative;
  }
  .card {
    position: absolute;
    top: 257px;
    width: 500px;
    height: 286px;
    overflow: hidden;
    box-shadow: 0 10px 24px rgba(150, 110, 40, 0.25);
  }
  /* Front */
  .card-front {
    left: 70px;
    background: var(--teal);
    display: flex;
    flex-direction: column;
    align-items: center;
    justify-content: center;
    color: var(--white);
  }
  .brand-mark {
    width: 70px;
    height: 70px;
    border: 4px solid var(--white);
    border-radius: 50%;
    margin-bottom: 14px;
  }
  .brand-name {
    font-size: 30px;
    font-weight: 400;
    letter-spacing: 3px;
    text-transform: uppercase;
    text-align: center;
    line-height: 1.15;
    color: var(--white);
  }
  .tagline {
    margin-top: 10px;
    font-size: 13px;
    letter-spacing: 2px;
    text-transform: uppercase;
    color: var(--gold);
  }
  /* Back */
  .card-back { left: 630px; background: var(--teal); }
  .name-panel {
    height: 128px;
    background: var(--white);
    display: flex;
    flex-direction: column;
    align-items: center;
    justify-content: flex-end;
    padding-bottom: 20px;
    color: var(--ink);
  }
  .person-name {
    font-size: 22px;
    font-weight: 700;
    letter-spacing: 1px;
    text-transform: uppercase;
    line-height: 1;
  }
  .person-title {
    font-size: 20px;
    font-style: italic;
    line-height: 1.1;
  }
  .contact-grid {
    display: grid;
    grid-template-columns: 225px 1fr;
    row-gap: 18px;
    column-gap: 10px;
    padding: 34px 16px 0 22px;
  }
  .contact-item {
    display: flex;
    align-items: center;
    gap: 9px;
    color: var(--white);
    font-size: 12px;
    line-height: 1.25;
  }
  .contact-icon {
    flex: 0 0 28px;
    width: 28px;
    height: 28px;
    border-radius: 50%;
    background: var(--gold);
    display: flex;
    align-items: center;
    justify-content: center;
  }
  .contact-icon svg { width: 16px; height: 16px; }
</style>
</head>
<body>
  <section class="card card-front" aria-label="Card front">
    <div class="brand-mark"></div>
    <h1 class="brand-name">Willowmere<br>Counseling</h1>
    <p class="tagline">Endure - Mend - Flourish</p>
  </section>

  <section class="card card-back" aria-label="Card back">
    <div class="name-panel">
      <p class="person-name">Your Name</p>
      <p class="person-title">Manager</p>
    </div>
    <div class="contact-grid">
      <div class="contact-item">
        <span class="contact-icon">
          <svg viewBox="0 0 16 16" fill="none" stroke="#3a9fbb" stroke-width="1.6" stroke-linecap="round"><path d="M2 6c0-2 2.5-3 6-3s6 1 6 3l-2.5 1-1-1.5h-5l-1 1.5z"/><path d="M4 13h8l-1-5H5z"/></svg>
        </span>
        <span>(214) 555-0187</span>
      </div>
      <div class="contact-item">
        <span class="contact-icon">
          <svg viewBox="0 0 16 16" fill="none" stroke="#3a9fbb" stroke-width="1.6" stroke-linecap="round"><circle cx="8" cy="6" r="4"/><circle cx="8" cy="6" r="1.5"/><path d="M5 13h6"/></svg>
        </span>
        <span>www.WillowmereCounseling.example</span>
      </div>
      <div class="contact-item">
        <span class="contact-icon">
          <svg viewBox="0 0 16 16" fill="none" stroke="#3a9fbb" stroke-width="1.6" stroke-linecap="round" stroke-linejoin="round"><path d="M8 15s-5-5-5-8.5a5 5 0 0 1 10 0C13 10 8 15 8 15z"/><circle cx="8" cy="6.5" r="1.8"/></svg>
        </span>
        <span>3870 N. Garrick Ave., Suite 214,<br>Fort Worth, TX 76132</span>
      </div>
      <div class="contact-item">
        <span class="contact-icon">
          <svg viewBox="0 0 16 16" fill="none" stroke="#3a9fbb" stroke-width="1.6" stroke-linejoin="round"><rect x="2" y="4" width="12" height="9"/><path d="M2 4l6 5 6-5"/></svg>
        </span>
        <span>info@WillowmereCounseling.example</span>
      </div>
    </div>
  </section>
</body>
</html>
```